Dental Practice based in Melbourne needs header designed for mobile website

Evergrove Dental Carlton needs logo modified (better color scheme)and the header needs good use of colors (Green should be one of them) . The overall scheme is attached below. Please maintain the overall position of the logo in the center just like the way it is. Icons that should be present : Evergrove Dental Carlton, Phone number with phone icon, Menu bar, Book now, search icon, Logo. in the center.

```html
<!DOCTYPE html>
<html lang="en">
<head>
<meta charset="utf-8">
<title>Evergrove Dental Carlton – Mobile Header</title>
<link rel="stylesheet" href="https://fonts.googleapis.com/css2?family=Open+Sans:ital,wght@0,400;0,600;0,700;1,400&display=swap">
<style>
  :root {
    --mint-bg: #e8fce9;
    --green: #5cc08a;
    --green-dark: #3f9f6d;
    --green-soft: #9fe0a8;
    --orange: #f0735a;
    --white: #ffffff;
    --placeholder: #9aa3a0;
  }
  * { box-sizing: border-box; margin: 0; padding: 0; }
  html, body { width: 1200px; height: 952px; overflow: hidden; }
  body { font-family: "Open Sans", Arial, sans-serif; background: var(--white); }

  .canvas { position: relative; width: 1200px; height: 952px; overflow: hidden; }

  .hero {
    position: absolute; left: 0; top: 230px; width: 1200px; height: 722px;
  }
  .hero-photo {
    position: absolute; inset: 0;
    background: radial-gradient(ellipse at 72% 40%, #8fd3a6 0%, #6cbf8f 40%, #4f9f78 100%);
  }
  .hero-content {
    position: absolute; left: 0; right: 0; top: 135px; text-align: center; color: var(--white);
  }
  .hero-title { font-weight: 600; font-size: 52px; line-height: 1.1; }
  .hero-tagline { font-size: 40px; line-height: 1.2; margin-top: 8px; }
  .book-btn {
    display: inline-block; margin-top: 52px; width: 216px; height: 54px; line-height: 54px;
    background: var(--orange); color: var(--white); border-radius: 6px;
    font-weight: 700; font-size: 24px; text-decoration: none;
  }

  .header {
    position: absolute; left: 0; top: 0; width: 1200px; height: 230px;
    background: var(--mint-bg); border-bottom: 8px solid var(--white);
  }
  .search {
    position: absolute; left: 375px; top: 40px; width: 450px; height: 52px;
    background: var(--white); border-radius: 6px; display: flex;
  }
  .search-input {
    flex: 1; padding-left: 24px; line-height: 52px;
    font-style: italic; font-size: 24px; color: var(--placeholder);
  }
  .search-btn {
    width: 58px; height: 52px; background: var(--green); border-radius: 0 6px 6px 0;
    display: flex; align-items: center; justify-content: center;
  }
  .menu-toggle { position: absolute; left: 1092px; top: 44px; }

  .brand-name {
    position: absolute; left: 34px; top: 141px; width: 450px;
    font-weight: 600; font-size: 30px; line-height: 42px;
    color: var(--green); white-space: nowrap;
  }

  .brand-badge {
    position: absolute; left: 505px; top: 112px; width: 190px; height: 190px;
    border-radius: 50%; background: var(--white);
    display: flex; align-items: center; justify-content: center;
  }
  .brand-badge-dot {
    width: 150px; height: 150px; border-radius: 50%; background: var(--green-soft);
  }

  .phone {
    position: absolute; left: 843px; top: 140px; display: flex; align-items: center; gap: 18px;
    color: var(--orange); font-weight: 600; font-size: 32px;
  }
</style>
</head>
<body>
<div class="canvas">
  <section class="hero">
    <div class="hero-photo" role="img" aria-label="Photo of a smiling young woman with long wavy hair and a scarf, tinted green"></div>
    <div class="hero-content">
      <h1 class="hero-title">Holistic Dentistry Approach</h1>
      <p class="hero-tagline">...for you, for your smile!</p>
      <a class="book-btn" href="#">BOOK NOW</a>
    </div>
  </section>

  <header class="header">
    <div class="search">
      <span class="search-input">Search</span>
      <span class="search-btn">
        <svg width="28" height="28" viewBox="0 0 28 28" aria-hidden="true">
          <circle cx="11" cy="11" r="7" fill="none" stroke="#fff" stroke-width="3.5"/>
          <line x1="16" y1="16" x2="24" y2="24" stroke="#fff" stroke-width="5" stroke-linecap="round"/>
        </svg>
      </span>
    </div>

    <svg class="menu-toggle" width="62" height="48" viewBox="0 0 62 48" aria-label="Menu">
      <rect x="0" y="0" width="62" height="8" rx="4" fill="var(--green)"/>
      <rect x="0" y="20" width="62" height="8" rx="4" fill="var(--green)"/>
      <rect x="0" y="40" width="62" height="8" rx="4" fill="var(--green)"/>
    </svg>

    <div class="brand-name">Evergrove Dental Carlton</div>

    <div class="phone">
      <svg width="38" height="38" viewBox="0 0 24 24" aria-hidden="true">
        <path fill="var(--green)" d="M6.6 10.8c1.4 2.8 3.8 5.1 6.6 6.6l2.2-2.2c.3-.3.7-.4 1-.2 1.1.4 2.3.6 3.6.6.6 0 1 .4 1 1V20c0 .6-.4 1-1 1C10.6 21 3 13.4 3 4c0-.6.4-1 1-1h3.5c.6 0 1 .4 1 1 0 1.3.2 2.5.6 3.6.1.3 0 .7-.2 1z"/>
      </svg>
      <span>0390001234</span>
    </div>
  </header>

  <div class="brand-badge"><div class="brand-badge-dot"></div></div>
</div>
</body>
</html>
```